Quillmere Business Advisory Business Card Design Project

I have a new business called Quillmere Business Advisory Limited. We provide business services for the UK for areas which include

Mentoring / Coaching
Interim Management
Non Executive Director / Chairman placement
Angel Investment support
Merger & Acquisition advice
Selling your business advice

I would like a background colour on the logo, a logo and our company name on the logo if possible.

I am open to colours but we want to portray a strong safe business with credibility

The business card design must match that of the logo design

Target Market(s)

SME and Medium size businesses with the owners, MD's, CEO or senior management as the target audiabce

Industry/Entity Type

Business

Requirements
Must have
• Match the logo design.
Look professional and quality
Should not have
• Old style text and colours
Poor logos depicting money

```html
<!DOCTYPE html>
<html lang="en">
<head>
<meta charset="utf-8">
<title>Quillmere Business Advisory – Business Cards</title>
<link rel="stylesheet" href="https://fonts.googleapis.com/css2?family=Open+Sans:wght@400;600&display=swap">
<style>
  :root {
    --backdrop: #a8a8ad;
    --card-dark: #060606;
    --card-light: #ffffff;
    --accent: #e87722;
    --ink: #3b3b3b;
    --ink-soft: #555555;
    --paper-text: #ffffff;
  }
  * { margin: 0; padding: 0; box-sizing: border-box; }
  html, body {
    width: 1200px; height: 863px; overflow: hidden;
    background: var(--backdrop);
    font-family: "Open Sans", Arial, sans-serif;
  }
  .canvas {
    position: relative; width: 1200px; height: 863px;
    display: flex; flex-direction: column; align-items: center; justify-content: center; gap: 40px;
  }
  .card {
    position: relative; width: 620px; height: 354px;
    box-shadow: 0 10px 24px rgba(0,0,0,.28);
  }
  .card--back { background: var(--card-dark); }
  .card--front { background: var(--card-light); }
  .edge-bar {
    position: absolute; width: 9px; height: 118px; background: var(--accent);
  }
  .edge-bar--left { left: 0; top: 30px; }
  .edge-bar--right { right: 0; bottom: 30px; }

  .brand {
    display: flex; align-items: center; gap: 14px;
  }
  .brand__dot {
    width: 30px; height: 30px; border-radius: 50%; background: var(--accent); flex: none;
  }
  .brand__name {
    font-weight: 600; font-size: 22px; letter-spacing: .5px; line-height: 1.2;
  }
  .card--back .brand {
    position: absolute; left: 0; right: 0; top: 150px; justify-content: center;
  }
  .card--back .brand__name { color: var(--paper-text); }

  .card--front .brand {
    position: absolute; left: 0; right: 0; top: 78px; justify-content: center;
  }
  .card--front .brand__name { color: var(--ink); }

  .details {
    position: absolute; left: 0; right: 0; top: 170px;
    display: flex; justify-content: center;
  }
  .person {
    text-align: right; padding-right: 18px; color: var(--ink-soft);
  }
  .person__name { font-size: 21px; color: var(--ink); line-height: 1.2; }
  .person__title { font-size: 15px; color: var(--ink); margin-bottom: 4px; }
  .person__address { font-size: 12.5px; line-height: 1.45; }
  .divider { width: 2px; height: 112px; background: var(--accent); margin-top: 4px; }
  .contact {
    padding-left: 18px; font-size: 14.5px; color: var(--ink); line-height: 1.3;
  }
  .contact__phones { margin-top: 36px; margin-bottom: 6px; }
</style>
</head>
<body>
  <main class="canvas">
    <section class="card card--back" aria-label="Business card back">
      <span class="edge-bar edge-bar--left"></span>
      <span class="edge-bar edge-bar--right"></span>
      <div class="brand">
        <span class="brand__dot"></span>
        <span class="brand__name">Quillmere Business Advisory Limited</span>
      </div>
    </section>

    <section class="card card--front" aria-label="Business card front">
      <span class="edge-bar edge-bar--left"></span>
      <span class="edge-bar edge-bar--right"></span>
      <div class="brand">
        <span class="brand__dot"></span>
        <span class="brand__name">Quillmere Business Advisory Limited</span>
      </div>
      <div class="details">
        <div class="person">
          <p class="person__name">Name Here</p>
          <p class="person__title">Title Here</p>
          <p class="person__address">Addressline one, Addressline two,<br>City, Zipcode</p>
        </div>
        <span class="divider"></span>
        <div class="contact">
          <p class="contact__phones">M: 000 000 0000<br>P: 000 000 0000<br>F: 000 000 0000</p>
          <p>info@domainname.com<br>www.domainname.com</p>
        </div>
      </div>
    </section>
  </main>
</body>
</html>
```